Keystone Nest Checks Inspection Report Stationary

I require some new stationary for my home inspection reports in PDF. A first page then second page and beyond. We have plenty of marketing material on our website to get an idea about us and I have attached a copy of what it looks like now and our logo's in EPS. Just looking for something a little more attractive than our plain stationary. www.keystonenestchecks.com

Target Market(s)

New home owners

Industry/Entity Type

Home Inspection

Font styles to use
Sans Serif

Colors
ec1f27

Requirements
Must have
• Our Keystone Nest Checks Colors
Nice to have
• sorry no clue
Should not have
• It can't bee too large becasue we are basically pasting our report in it.

```html
<!DOCTYPE html>
<html lang="en">
<head>
<meta charset="utf-8">
<title>Keystone Nest Checks – Inspection Report Page</title>
<link href="https://fonts.googleapis.com/css2?family=Source+Sans+3:wght@400;600;700&display=swap" rel="stylesheet">
<style>
  :root {
    --brand-red: #d4164a;
    --accent-red: #ec1f27;
    --bar-grey: #a5a5a5;
    --footer-grey: #8e8e8e;
    --text-dark: #2b2b2b;
    --white: #ffffff;
  }
  * { margin: 0; padding: 0; box-sizing: border-box; }
  html, body { width: 849px; height: 1200px; overflow: hidden; }
  body {
    font-family: "Source Sans 3", Arial, sans-serif;
    color: var(--text-dark);
    background: var(--white);
  }
  .page {
    position: relative;
    width: 849px;
    height: 1200px;
    background: linear-gradient(135deg, #f7f7f7 0%, #e9e9e9 35%, #f4f4f4 60%, #e6e6e6 100%);
    overflow: hidden;
  }
  .page-header {
    position: absolute; left: 0; top: 0; width: 849px; height: 144px;
    background: var(--white);
  }
  .brand {
    position: absolute; left: 26px; top: 44px;
    display: flex; align-items: center; gap: 10px;
  }
  .brand-mark { width: 30px; height: 30px; background: var(--brand-red); }
  .brand-name {
    font-size: 27px; font-weight: 600; color: var(--brand-red); letter-spacing: 0.3px;
  }
  .brand-tagline {
    position: absolute; left: 70px; top: 98px;
    font-size: 14px; color: var(--brand-red);
  }
  .property-address {
    position: absolute; right: 40px; top: 40px;
    font-size: 20px; font-weight: 700; color: var(--brand-red);
  }
  .header-rule {
    position: absolute; left: 0; top: 142px; width: 849px; height: 2px;
    background: var(--brand-red);
  }
  .section-bar {
    position: absolute; left: 51px; width: 744px; height: 26px;
    background: var(--bar-grey); color: var(--white);
    font-size: 16px; font-weight: 700; text-align: center; line-height: 26px;
  }
  .section-notes {
    position: absolute; left: 51px; width: 744px;
    font-size: 13.5px; line-height: 18.5px; text-align: center;
  }
  .photo {
    position: absolute;
    background: linear-gradient(180deg, #8c9198 0%, #b7bcc2 45%, #eef0f3 100%);
  }
  .callout {
    position: absolute; left: 557px; top: 683px; width: 238px; height: 310px;
    background: var(--brand-red); color: var(--white);
    padding: 48px 22px 0 24px;
    font-size: 15px; line-height: 19px;
  }
  .callout strong { font-weight: 700; }
  .page-footer {
    position: absolute; left: 0; top: 1146px; width: 849px; height: 54px;
    background: var(--footer-grey); color: var(--white);
    font-size: 18px; font-weight: 700; text-align: center; line-height: 54px;
  }
</style>
</head>
<body>
<div class="page">
  <header class="page-header">
    <div class="brand">
      <span class="brand-mark"></span>
      <span class="brand-name">Keystone Nest Checks</span>
    </div>
    <div class="brand-tagline">Thorough Eyes. Honest Answers.</div>
    <div class="property-address">418 Larkspur Crescent NE, Calgary, AB</div>
    <div class="header-rule"></div>
  </header>

  <div class="section-bar" style="top:161px">4. Stairs &amp; Handrail</div>
  <div class="section-notes" style="top:190px">
    Observations:<br>
    • Wood Railing<br>
    • Appeared functional at time of inspection.
  </div>

  <div class="section-bar" style="top:255px">5. Patio Comments</div>
  <div class="section-notes" style="top:283px">
    Materials: Concrete patio noted. • Brick/Paving Stones Decking<br>
    Observations:<br>
    • Appears in satisfactory and functional condition with normal wear for its age.<br>
    • Due to snow or ice cover, the comments reflect only the visible portion of the lots and grounds.
  </div>

  <div class="photo" style="left:51px;top:362px;width:365px;height:270px" role="img" aria-label="Photo of snow-covered concrete side patio with steps beside the house"></div>
  <div class="photo" style="left:436px;top:362px;width:359px;height:270px;background:linear-gradient(160deg,#7a6a5e 0%,#a46a55 40%,#e8eaee 100%)" role="img" aria-label="Photo of snowy patio table and red brick paving stone walkway"></div>

  <div class="section-bar" style="top:645px">6. Fence Condition</div>
  <div class="photo" style="left:51px;top:683px;width:506px;height:310px;background:linear-gradient(180deg,#6f7a82 0%,#9aa3ab 40%,#eef0f3 70%,#f7f8fa 100%)" role="img" aria-label="Photo of grey wooden fence around a snow-covered backyard"></div>
  <div class="callout">
    <strong>Materials:</strong> Wood<br>
    <strong>Observations:</strong><br>
    • Appeared serviceable and solid at time of inspection. A Home Inspection does not include the inspection of the footings. It is only a visual inspection. If there are concerns with these limitations we recommend having a qualified contractor evaluate further.
  </div>

  <div class="section-bar" style="top:1014px">7. Gates</div>
  <div class="section-notes" style="top:1043px">
    Materials: Wood<br>
    Conditions:<br>
    • Gate(s) was in good condition at time of inspection.
  </div>

  <footer class="page-footer">Page 5 of 50</footer>
</div>
</body>
</html>
```